Auto Tuning Shop needs an advertising design

An advertising design that can be used online for marketing on Facebook, Google, Instagram. A picture that says exactly what we do - window tinting / car window films. Looks professional and is informative. But not too much content and text.
Possibly a picture of the car looks like window tint from the outside (very dark), but when sitting in the car you have a perfect view of the outside.
Passwords in picture: UV protection, heat protection, burglary protection, privacy protection
Not too many colors.

Here are a few sample pictures as we often designed it ourselves, but it has to look more professional.

Target Market(s)

Reach new customers because it is a campaign / offer

Requirements
Must have
• German language
Nice to have
• Passwords in picture: UV protection, heat protection, burglary protection, privacy protection

```html
<!DOCTYPE html>
<html lang="de">
<head>
<meta charset="utf-8">
<title>Veltro – Professionelle Scheibentönung</title>
<link rel="stylesheet" href="https://fonts.googleapis.com/css2?family=Russo+One&family=Exo+2:ital,wght@1,700;1,900&family=Rajdhani:wght@500;600;700&display=swap">
<style>
  :root {
    --page: #ececec;
    --black: #0c0c0d;
    --charcoal: #1c1c1e;
    --red: #d7161f;
    --red-deep: #7a0a10;
    --white: #f4f4f4;
    --gold-light: #f6dc7c;
    --gold: #d4ae3f;
    --gold-dark: #a8801f;
  }
  * { margin: 0; padding: 0; box-sizing: border-box; }
  html, body { width: 1200px; height: 900px; overflow: hidden; background: var(--page); }
  .ad {
    position: absolute; left: 170px; top: 23px; width: 860px; height: 854px;
    background: radial-gradient(ellipse at 50% 70%, #222224 0%, var(--black) 70%);
    overflow: hidden; font-family: "Rajdhani", sans-serif;
  }
  .ad > * { position: absolute; }
  .decor { left: 0; top: 0; width: 860px; height: 854px; }
  .title-band {
    left: 275px; top: 0; width: 585px; height: 160px;
    background: linear-gradient(100deg, var(--red) 0%, #b3121a 45%, var(--red-deep) 100%);
    clip-path: polygon(63px 0, 100% 0, 100% 100%, 0 100%);
  }
  .title {
    left: 340px; top: 26px; width: 510px; text-align: center;
    font-family: "Russo One", sans-serif; font-size: 55px; line-height: 62px;
    color: var(--white); letter-spacing: -0.5px; text-shadow: 0 3px 4px rgba(0,0,0,.55);
  }
  .brand { left: 44px; top: 62px; display: flex; align-items: center; gap: 12px; }
  .brand-dot { width: 30px; height: 30px; border-radius: 50%; background: var(--red); }
  .brand-name {
    font-family: "Russo One", sans-serif; font-size: 42px; color: var(--red); letter-spacing: 1px;
  }
  .kicker {
    left: 66px; top: 206px; font-family: "Exo 2", sans-serif; font-style: italic; font-weight: 700;
    font-size: 34px; letter-spacing: 2px; color: var(--white);
  }
  .headline {
    left: 62px; top: 244px; font-family: "Exo 2", sans-serif; font-style: italic; font-weight: 900;
    font-size: 92px; line-height: 100px; letter-spacing: -1px; white-space: nowrap;
    background: linear-gradient(180deg, var(--gold-light) 0%, var(--gold) 50%, var(--gold-dark) 100%);
    -webkit-background-clip: text; background-clip: text; color: transparent;
  }
  .sub-band {
    left: 172px; top: 344px; width: 613px; height: 52px; background: var(--red);
    clip-path: polygon(22px 0, 100% 0, calc(100% - 22px) 100%, 0 100%);
  }
  .sub-title {
    left: 172px; top: 344px; width: 613px; height: 52px; line-height: 52px; text-align: center;
    font-family: "Russo One", sans-serif; font-style: italic; font-size: 38px; color: var(--white);
    letter-spacing: 1px;
  }
  .benefits {
    left: 0; width: 860px; list-style: none; display: flex; justify-content: center; gap: 16px;
    font-size: 27px; font-weight: 500; color: var(--white);
  }
  .benefits li::before { content: "\25CF"; color: var(--red); font-size: 18px; margin-right: 12px; vertical-align: 3px; }
  .benefits-1 { top: 428px; }
  .benefits-2 { top: 464px; }
  .car-photo {
    left: 36px; top: 548px; width: 664px; height: 236px; border-radius: 90px 140px 30px 30px;
    background: linear-gradient(180deg, #1e1e20 0%, #2a2a2c 30%, #b4141c 45%, #c8181f 75%, #5a0a0e 100%);
  }
  .compare {
    left: 720px; width: 106px; height: 106px; border-radius: 50%; border: 3px solid var(--red);
  }
  .compare-before { top: 508px; background: linear-gradient(160deg, #8a8d90 0%, #3b3e41 60%, #161618 100%); }
  .compare-after { top: 647px; background: linear-gradient(160deg, #1a1a1b 0%, #050505 60%, #8b0f15 100%); }
  .compare-label {
    left: 720px; width: 106px; text-align: center; font-size: 15px; font-weight: 600; color: var(--red);
  }
  .label-before { top: 618px; }
  .label-after { top: 760px; }
  .contact {
    left: 0; top: 808px; width: 860px; text-align: center; font-weight: 700; font-size: 19px;
    letter-spacing: 2.5px; color: var(--gold);
  }
  .contact .sep { margin: 0 26px; color: var(--gold-light); }
</style>
</head>
<body>
<main class="ad">
  <svg class="decor" viewBox="0 0 860 854" aria-hidden="true">
    <polygon points="0,400 0,460 150,560 210,560" fill="#1f1f21"/>
    <polygon points="860,450 860,480 640,600 600,600" fill="#1f1f21"/>
    <line x1="0" y1="470" x2="110" y2="570" stroke="#c4141c" stroke-width="2"/>
    <line x1="92" y1="470" x2="165" y2="540" stroke="#c4141c" stroke-width="1.5"/>
    <line x1="820" y1="500" x2="600" y2="640" stroke="#c4141c" stroke-width="1.5"/>
  </svg>

  <div class="brand">
    <span class="brand-dot"></span>
    <span class="brand-name">VELTRO</span>
  </div>

  <div class="title-band"></div>
  <h1 class="title">PROFESSIONELLE<br>SCHEIBENTONUNG</h1>

  <p class="kicker">GERMAN QUALITY OF</p>
  <h2 class="headline">WINDOW TINTING</h2>

  <div class="sub-band"></div>
  <p class="sub-title">CAR WINDOW FILMS</p>

  <ul class="benefits benefits-1">
    <li>Sonnenschutzverglasung</li>
    <li>Scheibenfolierung</li>
  </ul>
  <ul class="benefits benefits-2">
    <li>UV und Hitze - Schutz</li>
    <li>Splitterschutz</li>
  </ul>

  <div class="car-photo" role="img" aria-label="Foto: roter Kompaktwagen in Seitenansicht mit dunkel getönten Scheiben"></div>

  <div class="compare compare-before" role="img" aria-label="Foto: Autoscheibe vor der Tönung"></div>
  <p class="compare-label label-before">Before</p>
  <div class="compare compare-after" role="img" aria-label="Foto: Autoscheibe nach der Tönung"></div>
  <p class="compare-label label-after">After</p>

  <p class="contact">0170 48213 596<span class="sep">|</span>WWW.VELTRO-FOLIE.DE<span class="sep">|</span>INFO@VELTRO-FOLIE.DE</p>
</main>
</body>
</html>
```